Redesign of an educational Eye website for Medical Students and Healthcare professionals

www.corvantisportal.com is an educational resource, illustrated using high quality 3D animations, for undergraduate medical students and healthcare professionals to learn about the anatomy of the human eye and associated common eye disorders.

The website was originally developed (using a Joomla template) a couple of years ago and we now want to update the brand and design of the site. Example content and animations can be found at https://www.corvantisportal.com/overview or https://www.corvantisportal.com/ocular-anatomy/orbital-anatomy

We would like a new logo and home page design (to include new colour palette, fonts and updated overall design).

The attached PowerPoint contains an example layout of the revised components we want to appear on the new Home page. We plan to have a hero panel at the top of page playing a short video of some of the animations. Similar to how this site works (www.zembri.uk.com).

We want the new site to feel Professional, Modern and Clean and simple.

Target Market(s)

Undergraduate medical students and Healthcare Professionals

Industry/Entity Type

Medical

Logo Text

Corvantis Portal

Number of Pages Required

1 page

Font styles to use
Sans Serif

Colors

Designer to choose colors to be used in the design.

```html
<!DOCTYPE html>
<html lang="en">
<head>
<meta charset="utf-8">
<title>Corvantis Portal</title>
<link rel="stylesheet" href="https://fonts.googleapis.com/css2?family=Lato:wght@400;700;900&display=swap">
<style>
:root{
  --navy:#1b2a6b;
  --blue:#1e7fd0;
  --sky:#2a8de0;
  --hero:#1f6fd6;
  --ink:#2b2b2b;
  --muted:#555;
  --grey:#efefef;
  --footer:#222426;
  --white:#fff;
  --gold:#d9a51e;
}
*{box-sizing:border-box;margin:0;padding:0}
html,body{width:1200px;height:3939px;overflow:hidden}
body{font-family:'Lato',sans-serif;color:var(--ink);background:var(--white);position:relative}
.abs{position:absolute}
.header{top:0;left:0;width:1200px;height:82px;background:var(--white)}
.brand{left:75px;top:22px;display:flex;align-items:center;gap:8px;font-size:28px;font-weight:700;color:var(--navy)}
.brand .dot{width:16px;height:16px;border-radius:50%;background:var(--blue)}
.nav{right:75px;top:24px;display:flex;align-items:center;gap:38px;font-size:15px;font-weight:700;color:#333}
.nav .active{color:var(--navy)}
.signin{background:var(--blue);color:var(--white);padding:10px 30px;border-radius:22px}
.hero{top:82px;left:0;width:1200px;height:593px;background:linear-gradient(180deg,#2a7fe0 0%,#1d5fcc 100%)}
.hero h1{position:absolute;top:170px;width:100%;text-align:center;color:var(--white);font-size:46px;font-weight:900;letter-spacing:.5px}
.hero p{position:absolute;top:232px;left:160px;width:880px;text-align:center;color:var(--white);font-size:19px;font-weight:700;line-height:30px}
.play{position:absolute;left:572px;top:338px}
.hero-btn{position:absolute;top:420px;height:54px;width:362px;border-radius:27px;background:var(--navy);color:var(--white);font-size:18px;font-weight:700;display:flex;align-items:center;justify-content:center}
.trusted{top:722px;width:1200px;text-align:center;font-size:14px;font-weight:900;letter-spacing:.5px}
.partner{top:780px;height:100px;border-radius:6px;background:#e4e6ee}
h2.sec{position:absolute;width:1200px;text-align:center;font-size:34px;font-weight:700;color:#333}
.why{left:75px;top:950px;font-size:34px;font-weight:700;color:#333}
.band{top:940px;left:0}
.feat h3{font-size:28px;font-weight:700;color:var(--white);margin-bottom:22px}
.feat p{color:var(--white);font-size:17px;margin-bottom:8px}
.feat ul{list-style:none}
.feat li{color:var(--white);font-size:17px;line-height:33px;display:flex;align-items:center;gap:14px}
.feat li svg{flex:none}
.media{border:4px solid #9fb7e6}
.card{top:1978px;width:330px;height:282px;border:2px solid #d3d3d3;border-radius:10px;text-align:center;padding-top:22px}
.card h4{color:var(--blue);font-size:22px;font-weight:700;margin:14px 0 8px}
.card p{font-size:15px;line-height:22px;color:#333;padding:0 34px;height:70px}
.card .more{display:inline-block;margin-top:10px;border:2px solid var(--navy);border-radius:18px;padding:7px 32px;font-size:14px;color:var(--navy)}
.team{top:2295px;left:0;width:1200px;height:475px;background:var(--grey)}
.member{top:2458px;width:240px;text-align:center}
.avatar{width:182px;height:182px;border-radius:50%;margin:0 auto 20px;border:4px solid #cfd6e2;background:linear-gradient(160deg,#cfd6dd,#8d9aa8)}
.member h5{color:var(--blue);font-size:20px;font-weight:700}
.member span{font-size:15px}
.quote-photo{left:75px;top:2923px;width:184px;height:184px;border-radius:50%;border:4px solid #cfd6e2;background:linear-gradient(160deg,#d2d7de,#86929f)}
.quote{left:318px;top:2932px;width:810px}
.quote h5{color:var(--blue);font-size:20px;font-weight:700;margin-bottom:10px}
.quote .role{font-size:15px;margin-bottom:12px}
.quote p{font-size:15px;line-height:26px;color:#333}
.cta{top:3168px;left:0;width:1200px;height:287px;background:var(--navy)}
.cta h2{position:absolute;left:75px;top:58px;width:760px;text-align:center;color:var(--white);font-size:34px;font-weight:700}
.cta p{position:absolute;left:75px;top:108px;width:760px;text-align:center;color:var(--white);font-size:20px}
.cta .btn{position:absolute;left:337px;top:157px;width:232px;height:48px;border-radius:24px;background:var(--blue);color:var(--white);font-size:19px;font-weight:700;display:flex;align-items:center;justify-content:center}
.charity-h{top:3500px}
.charity-h em{font-style:normal;color:var(--blue)}
.charity{top:3582px;left:190px;width:820px;text-align:center;font-size:15px;line-height:26px}
.footer{top:3708px;left:0;width:1200px;height:231px;background:var(--footer);color:#ddd}
.fbrand{left:75px;top:45px;display:flex;align-items:center;gap:8px;font-size:28px;font-weight:700;color:var(--white)}
.fbrand .dot{width:16px;height:16px;border-radius:50%;background:var(--white)}
.copy{left:75px;top:125px;font-size:12px;line-height:19px;color:#bbb}
.fcol{top:45px;font-size:14px;line-height:28px;color:#ccc}
.fcol b{display:block;color:var(--sky);font-size:17px;font-weight:700;margin-bottom:4px}
.news{left:760px;top:45px}
.news b{display:block;color:var(--sky);font-size:17px;margin-bottom:14px}
.news .row{display:flex;gap:12px}
.news .field{width:250px;height:40px;border-radius:20px;background:var(--white);color:#777;font-size:14px;padding:11px 20px}
.news .go{width:104px;height:40px;border-radius:20px;background:var(--blue);color:var(--white);font-size:15px;font-weight:700;display:flex;align-items:center;justify-content:center}
.community{left:760px;top:160px;display:flex;align-items:center;gap:12px;color:var(--sky);font-size:17px;font-weight:700}
.community i{width:16px;height:16px;border-radius:50%;background:var(--white);display:inline-block}
</style>
</head>
<body>
<header class="abs header">
  <div class="abs brand"><span class="dot"></span>Corvantis Portal</div>
  <nav class="abs nav"><span class="active">HOME</span><span>ABOUT</span><span>CHAPTERS</span><span>FAQ</span><span>CONTACT</span><span class="signin">SIGN IN</span></nav>
</header>

<section class="abs hero" role="img" aria-label="Blue-toned background video still of a person wearing an eye mask">
  <h1>LEARN FASTER AND SMARTER</h1>
  <p>Corvantis Portal helps undergraduates and healthcare professionals to learn or update their knowledge about the clinically relevant anatomy, ophthalmic examination techniques and common eye disorders of the human eye.</p>
  <svg class="play" width="56" height="56" viewBox="0 0 56 56"><circle cx="28" cy="28" r="25" fill="none" stroke="#fff" stroke-width="4"/><path d="M22 16 L40 28 L22 40Z" fill="#fff"/></svg>
  <div class="hero-btn" style="left:226px">Undergraduates- Learn More</div>
  <div class="hero-btn" style="left:614px">Healthcare Professionals- Learn More</div>
</section>

<div class="abs trusted">TRUSTED ACROSS THE WORLD</div>
<div class="abs partner" style="left:222px;width:126px"></div>
<div class="abs partner" style="left:404px;width:86px"></div>
<div class="abs partner" style="left:548px;width:164px;background:#bcd8ee"></div>
<div class="abs partner" style="left:756px;width:228px"></div>

<div class="abs why">Why Corvantis Portal?</div>
<svg class="abs band" width="1200" height="900" viewBox="0 0 1200 900">
  <polygon points="0,110 1200,15 1200,390 0,505" fill="#1b2a6b"/>
  <polygon points="0,505 1200,390 1200,760 0,900" fill="#1e7fd0"/>
</svg>

<div class="abs feat" style="left:75px;top:1118px;width:560px">
  <h3>Credible</h3>
  <p>Written and illustrated by experienced Consultant Ophthalmologists</p>
  <ul>
    <li><svg width="16" height="14"><path d="M2 7 L6 11 L14 2" stroke="#fff" stroke-width="3" fill="none"/></svg>Concise text and structured content</li>
    <li><svg width="16" height="14"><path d="M2 7 L6 11 L14 2" stroke="#fff" stroke-width="3" fill="none"/></svg>Practical clinical emphasis</li>
    <li><svg width="16" height="14"><path d="M2 7 L6 11 L14 2" stroke="#fff" stroke-width="3" fill="none"/></svg>Each core topic distilled to the essential learning points</li>
  </ul>
</div>
<div class="abs media" style="left:670px;top:1082px;width:415px;height:236px;background:linear-gradient(135deg,#c9916c,#6b4a3a 60%,#3a4a4a)" role="img" aria-label="3D illustration of eye drops being applied to an eye"></div>

<div class="abs media" style="left:110px;top:1472px;width:412px;height:236px;background:linear-gradient(160deg,#c79078,#9a6a58 55%,#5a3a30)" role="img" aria-label="3D animation still of a pair of eyes"></div>
<div class="abs feat" style="left:598px;top:1482px;width:520px">
  <h3>Visual</h3>
  <p>Over 70 stunning 3D animations</p>
  <ul>
    <li><svg width="16" height="14"><path d="M2 7 L6 11 L14 2" stroke="#fff" stroke-width="3" fill="none"/></svg>Show movement around and inside the eye</li>
    <li><svg width="16" height="14"><path d="M2 7 L6 11 L14 2" stroke="#fff" stroke-width="3" fill="none"/></svg>Help bring key concepts to life</li>
    <li><svg width="16" height="14"><path d="M2 7 L6 11 L14 2" stroke="#fff" stroke-width="3" fill="none"/></svg>Lorem ipsum</li>
  </ul>
</div>

<h2 class="sec" style="top:1858px">Training Modules</h2>
<div class="abs card" style="left:75px">
  <svg width="84" height="76" viewBox="0 0 84 76"><path d="M6 46 Q42 14 78 46 Q42 74 6 46Z" fill="none" stroke="#333" stroke-width="4"/><circle cx="42" cy="46" r="13" fill="#333"/><path d="M42 4 Q50 18 42 24 Q34 18 42 4Z" fill="#333"/></svg>
  <h4>Core Principles</h4>
  <p>Covers clinically relevant anatomy, fundamental topics and examination techniques in Ophthalmology.</p>
  <span class="more">Learn More</span>
</div>
<div class="abs card" style="left:436px">
  <svg width="84" height="76" viewBox="0 0 84 76"><circle cx="26" cy="14" r="9" fill="#333"/><rect x="16" y="26" width="20" height="30" rx="4" fill="#333"/><rect x="18" y="56" width="6" height="18" fill="#333"/><rect x="28" y="56" width="6" height="18" fill="#333"/><circle cx="60" cy="24" r="8" fill="#333"/><rect x="50" y="35" width="20" height="24" rx="4" fill="#333"/><rect x="44" y="58" width="32" height="5" fill="#333"/><rect x="48" y="62" width="5" height="12" fill="#333"/><rect x="68" y="62" width="5" height="12" fill="#333"/></svg>
  <h4>Ophthalmology in Practice</h4>
  <p>Deals with common eye disorders regularly encountered by healthcare professionals.</p>
  <span class="more">Learn More</span>
</div>
<div class="abs card" style="left:796px">
  <svg width="84" height="76" viewBox="0 0 84 76"><circle cx="36" cy="34" r="24" fill="none" stroke="#333" stroke-width="5"/><path d="M20 34 Q36 20 52 34 Q36 48 20 34Z" fill="#333"/><circle cx="36" cy="34" r="5" fill="#fff"/><path d="M54 52 L72 70" stroke="#333" stroke-width="8" stroke-linecap="round"/></svg>
  <h4>AN Other</h4>
  <p>Aliquam molestie, mi et imperdiet euismod, dui purus auctor tellus, et interdum lacus lectus et ante.</p>
  <span class="more">Learn More</span>
</div>

<section class="abs team">
  <h2 class="sec" style="top:62px">Meet the Team</h2>
</section>
<div class="abs member" style="left:120px"><div class="avatar" role="img" aria-label="Portrait photo of team member"></div><h5>Aldo Pemberly</h5><span>Consultant Ophthalmologist</span></div>
<div class="abs member" style="left:480px"><div class="avatar" role="img" aria-label="Portrait photo of team member"></div><h5>Tomas Reyvali</h5><span>Consultant Ophthalmologist</span></div>
<div class="abs member" style="left:838px"><div class="avatar" role="img" aria-label="Portrait photo of team member"></div><h5>Neil Brackon</h5><span>CTO</span></div>

<h2 class="sec" style="top:2826px">What People are Saying About Corvantis Portal?</h2>
<div class="abs quote-photo" role="img" aria-label="Portrait photo of reviewer"></div>
<div class="abs quote">
  <h5>Mr Owen Darcliffe MB ChB FRCOphth</h5>
  <div class="role">Consultant Ophthalmologist and Head of the School of Ophthalmology, Westmoor Deanery HEWM</div>
  <p>What sets this website apart are the superb 3D animations which enhance the accompanying text more effectively than clinical videos or photographs. I would whole heartedly recommend it to medical students, optometrists, GP's, casualty doctors and ophthalmic nurse practitioners, both as an introduction to ophthalmology, but also to refresh their knowledge of core ophthalmic examination techniques and conditions.</p>
</div>

<section class="abs cta">
  <h2>Want to try Corvantis Portal for free?</h2>
  <p>No credit card details required. It's completely free for 7 days</p>
  <div class="btn">Start Free Trial</div>
  <svg class="abs" style="left:852px;top:25px" width="236" height="236" viewBox="0 0 236 236"><circle cx="118" cy="118" r="114" fill="#d9a51e"/><circle cx="118" cy="118" r="90" fill="#b88712"/></svg>
</section>

<h2 class="sec charity-h">We Give <em>10%</em> of Our Profits to Charity</h2>
<p class="abs charity">We believe it is important to give something back so from 2018 we will donate 10% of every subscription to a selected charity somewhere in the world which works to help prevent sight loss and treat eye diseases.</p>

<footer class="abs footer">
  <div class="abs fbrand"><span class="dot"></span>Corvantis Portal</div>
  <div class="abs copy">Copyright © 2018, Company Name.<br>All Right Reserved</div>
  <div class="abs fcol" style="left:372px"><b>Company</b>About<br>Blog</div>
  <div class="abs fcol" style="left:538px"><b>Policies</b>Terms of Use<br>Privacy and Cookies</div>
  <div class="abs news"><b>Newsletter</b><div class="row"><div class="field">Enter Email Address</div><div class="go">Sign Up</div></div></div>
  <div class="abs community">Community <i></i><i></i><i></i></div>
</footer>
</body>
</html>
```